Company E-mail Signature

Hello!

I know what I want to do for our company's updated e-mail signature (Please see attached "Autumn 2023 email sig edit"). However, my skills are exceptionally limited and I am unable to work out, or find information on converting this into an e-mail signature, with clickable social media links.
This is for Microsoft Outlook and would need to be edited for 11 members of staff.
All help or any slight improvement suggestions are most welcome!

```html
<!DOCTYPE html>
<html lang="en">
<head>
<meta charset="utf-8">
<title>Harbourline Travel – Email Signature</title>
<link href="https://fonts.googleapis.com/css2?family=Poppins:wght@400;500;600;700&display=swap" rel="stylesheet">
<style>
  :root {
    --brown: #3a2208;
    --icon: #2a1a08;
    --gold: #c9a93a;
    --gold-light: #d8bf3a;
    --ink: #1c1c1c;
    --rule: #4a4a4a;
    --paper: #ffffff;
    --photo-top: #8b8480;
    --photo-mid: #a86a30;
    --photo-low: #5a4a3e;
    --photo-ground: #8e8a86;
  }
  * { margin: 0; padding: 0; box-sizing: border-box; }
  html, body { width: 1108px; height: 1200px; overflow: hidden; background: var(--paper); }
  body { font-family: "Poppins", sans-serif; color: var(--ink); position: relative; }

  .brand-tile {
    position: absolute; left: 44px; top: 86px; width: 285px; height: 285px;
    background: var(--brown);
    display: flex; align-items: center; justify-content: center;
  }
  .brand-name { color: var(--gold); font-weight: 700; font-size: 36px; letter-spacing: 0.5px; }

  .divider { position: absolute; left: 363px; top: 54px; width: 2px; height: 356px; background: var(--rule); }

  .person { position: absolute; left: 402px; top: 46px; }
  .person-name { color: var(--gold); font-weight: 700; font-size: 42px; line-height: 1.1; }
  .person-role { font-weight: 500; font-size: 24px; line-height: 1.3; margin-top: 2px; }

  .contact { position: absolute; left: 403px; top: 166px; list-style: none; }
  .contact li { font-size: 23px; line-height: 41px; white-space: nowrap; }
  .contact .label { color: var(--gold); font-weight: 600; margin-right: 8px; }

  .social { position: absolute; left: 405px; top: 322px; display: flex; gap: 14px; }
  .social a {
    display: flex; align-items: center; justify-content: center;
    width: 66px; height: 66px;
    background: linear-gradient(180deg, var(--gold-light), var(--gold));
  }
  .social svg { width: 30px; height: 30px; }

  .fleet-photo {
    position: absolute; left: 45px; top: 433px; width: 1021px; height: 360px;
    background: linear-gradient(180deg, var(--photo-top) 0%, var(--photo-mid) 30%, var(--photo-low) 60%, var(--photo-ground) 78%, var(--photo-ground) 100%);
  }

  .notice-title { position: absolute; left: 52px; top: 832px; font-size: 32px; font-weight: 700; color: var(--brown); }
  .rule { position: absolute; left: 50px; width: 1016px; height: 3px; background: var(--ink); }
  .rule-top { top: 890px; }
  .rule-bottom { top: 1077px; }

  .notice-list { position: absolute; left: 58px; top: 912px; width: 1000px; list-style: none; }
  .notice-list li { position: relative; padding-left: 31px; font-size: 21px; line-height: 26px; margin-bottom: 15px; }
  .notice-list li::before {
    content: ""; position: absolute; left: 0; top: 7px; width: 14px; height: 14px; border-radius: 50%; background: var(--ink);
  }

  .sign-off { position: absolute; left: 52px; top: 1094px; font-size: 30px; font-weight: 700; color: var(--brown); }
</style>
</head>
<body>
  <div class="brand-tile"><span class="brand-name">Harbourline</span></div>
  <div class="divider"></div>

  <div class="person">
    <div class="person-name">Daniel Marsh</div>
    <div class="person-role">Manager</div>
  </div>

  <ul class="contact">
    <li><span class="label">P:</span>0207 555 0148</li>
    <li><span class="label">E:</span>daniel.marsh@harbourline-travel.co.uk</li>
    <li><span class="label">W:</span>www.harbourline-travel.co.uk</li>
  </ul>

  <nav class="social" aria-label="Social media">
    <a href="#" aria-label="Social profile one">
      <svg viewBox="0 0 24 24" fill="none" stroke="var(--icon)" stroke-width="2.4" stroke-linecap="round" stroke-linejoin="round"><path d="M14 4h6v6"/><path d="M20 4l-9 9"/><path d="M18 14v5a1 1 0 0 1-1 1H5a1 1 0 0 1-1-1V7a1 1 0 0 1 1-1h5"/></svg>
    </a>
    <a href="#" aria-label="Social profile two">
      <svg viewBox="0 0 24 24" fill="none" stroke="var(--icon)" stroke-width="2.4" stroke-linecap="round" stroke-linejoin="round"><path d="M14 4h6v6"/><path d="M20 4l-9 9"/><path d="M18 14v5a1 1 0 0 1-1 1H5a1 1 0 0 1-1-1V7a1 1 0 0 1 1-1h5"/></svg>
    </a>
    <a href="#" aria-label="Social profile three">
      <svg viewBox="0 0 24 24" fill="none" stroke="var(--icon)" stroke-width="2.4" stroke-linecap="round" stroke-linejoin="round"><path d="M14 4h6v6"/><path d="M20 4l-9 9"/><path d="M18 14v5a1 1 0 0 1-1 1H5a1 1 0 0 1-1-1V7a1 1 0 0 1 1-1h5"/></svg>
    </a>
  </nav>

  <div class="fleet-photo" role="img" aria-label="Two brown Harbourline coaches parked facing each other in a car park with autumn trees behind"></div>

  <h2 class="notice-title">Important</h2>
  <div class="rule rule-top"></div>
  <ul class="notice-list">
    <li>Please note all quotations are valid for five days only.</li>
    <li>As part of our drive to become a Carbon Neutral Company, for every booking made, Harbourline will plant a tree on your behalf to offset our footprint.</li>
    <li>Please consider the environment before printing this email.</li>
  </ul>
  <div class="rule rule-bottom"></div>
  <p class="sign-off">Thank You</p>
</body>
</html>
```